Marlowbeck Media Stationary

Start up company requires matching stationary templates for Business Cards, letterhead and 'With Compliments' slips. The final design should keep with the style of our kiosk design, investor brochure and other collateral.

```html
<!DOCTYPE html>
<html lang="en">
<head>
<meta charset="utf-8">
<title>Marlowbeck Media – Business Card</title>
<link href="https://fonts.googleapis.com/css2?family=Didact+Gothic&display=swap" rel="stylesheet">
<style>
  :root {
    --brand-blue: #1b78b8;
    --card-white: #f3f3f3;
    --ink: #3a3a3a;
    --ink-soft: #5a5a5a;
    --backdrop: #e4e4e2;
    --white: #ffffff;
  }
  * { box-sizing: border-box; margin: 0; padding: 0; }
  html, body {
    width: 1200px; height: 900px; overflow: hidden;
    background: var(--backdrop);
    font-family: "Didact Gothic", "Century Gothic", sans-serif;
  }
  .sheet {
    width: 1200px; height: 900px;
    display: flex; flex-direction: column; align-items: center; justify-content: center;
    gap: 40px;
  }
  .card {
    width: 700px; height: 400px; position: relative; overflow: hidden;
    box-shadow: 0 6px 18px rgba(0,0,0,0.18);
  }

  /* Front */
  .card-front { background: var(--brand-blue); display: flex; align-items: center; justify-content: center; }
  .brand { display: flex; align-items: center; gap: 18px; }
  .brand-mark { width: 56px; height: 56px; background: var(--white); }
  .brand-name {
    font-size: 40px; letter-spacing: 2px; text-transform: uppercase; color: var(--white);
  }

  /* Back */
  .card-back { background: var(--card-white); }
  .side-band { position: absolute; left: 0; top: 0; width: 100px; height: 100%; background: var(--brand-blue); }
  .back-mark { position: absolute; left: 28px; top: 26px; width: 46px; height: 46px; background: var(--white); }
  .back-name {
    position: absolute; left: 118px; top: 32px;
    font-size: 30px; letter-spacing: 1.5px; text-transform: uppercase; color: var(--brand-blue);
  }
  .holder { position: absolute; left: 118px; top: 110px; }
  .holder-name { font-size: 15px; letter-spacing: 3px; text-transform: uppercase; color: var(--ink); }
  .holder-role { font-size: 14px; letter-spacing: 2px; color: var(--brand-blue); margin-top: 4px; }

  .contact { position: absolute; left: 290px; top: 205px; color: var(--ink); font-size: 15px; letter-spacing: 2px; }
  .contact-address { margin-left: 34px; margin-bottom: 14px; }
  .contact-list { list-style: none; }
  .contact-list li { display: flex; align-items: center; gap: 16px; height: 26px; }
  .contact-list svg { width: 16px; height: 16px; flex: none; }
</style>
</head>
<body>
<main class="sheet">
  <section class="card card-front" aria-label="Business card front">
    <div class="brand">
      <span class="brand-mark"></span>
      <span class="brand-name">Marlowbeck Media</span>
    </div>
  </section>

  <section class="card card-back" aria-label="Business card back">
    <div class="side-band"></div>
    <span class="back-mark"></span>
    <div class="back-name">Marlowbeck Media</div>

    <div class="holder">
      <div class="holder-name">Jonas Keller</div>
      <div class="holder-role">CEO</div>
    </div>

    <div class="contact">
      <div class="contact-address">Lindenweg 12, 8004 Zurich, Switzerland</div>
      <ul class="contact-list">
        <li>
          <svg viewBox="0 0 16 16" aria-hidden="true"><path d="M3 2h3l1 3-2 1.5a8 8 0 0 0 4.5 4.5L11 9l3 1v3a1 1 0 0 1-1 1A11 11 0 0 1 2 3a1 1 0 0 1 1-1z" fill="var(--brand-blue)"/></svg>
          <span>+41 44 210 48 30</span>
        </li>
        <li>
          <svg viewBox="0 0 16 16" aria-hidden="true"><rect x="4" y="1" width="8" height="14" rx="1.5" fill="none" stroke="var(--brand-blue)" stroke-width="1.6"/><circle cx="8" cy="12.5" r="0.9" fill="var(--brand-blue)"/></svg>
          <span>+41 78 406 92 17</span>
        </li>
        <li>
          <svg viewBox="0 0 16 16" aria-hidden="true"><rect x="1.5" y="3.5" width="13" height="9" fill="none" stroke="var(--brand-blue)" stroke-width="1.5"/><path d="M1.5 3.5 8 9l6.5-5.5" fill="none" stroke="var(--brand-blue)" stroke-width="1.5"/></svg>
          <span>jonas.keller@marlowbeck.ch</span>
        </li>
        <li>
          <svg viewBox="0 0 16 16" aria-hidden="true"><circle cx="8" cy="8" r="6.3" fill="none" stroke="var(--brand-blue)" stroke-width="1.5"/><path d="M1.7 8h12.6M8 1.7c-3 3.5-3 9.1 0 12.6M8 1.7c3 3.5 3 9.1 0 12.6" fill="none" stroke="var(--brand-blue)" stroke-width="1.2"/></svg>
          <span>www.marlowbeck.ch</span>
        </li>
      </ul>
    </div>
  </section>
</main>
</body>
</html>
```